Client Centric Brochure for Investment Advisory Firm

We need a client centric firm brochure that not only spotlights the services we provide as a wealth and investment management firm but also the value our expertise and expierience brings. We would like see designs that use this particular color green (RGB-0,92,51) and variations. Shouldn't be limited to this color however and are open to other color schemes Looking for something clean and consise. The final design should communicate financial safety, growth and reaching investment goals. Attached are rudimentary designs we have created, our company logo, and other source material. You can also visit our website www.harlowbendpartners.com for more inspiration.

Target Market(s)

Age Range - 35-65, Gender - 70% male, 30% female, Those looking to secure their financial future through wealth management and investing.

Industry/Entity Type

Investment

Font styles to use
Serif
Sans Serif

Colors
00a990

Requirements
Must have
• Project must have some of the information that was provided in the source documents. It must exhibit the client centric nature we are trying to exude.

```html
<!DOCTYPE html>
<html lang="en">
<head>
<meta charset="utf-8">
<title>Harlow Bend Partners – Brochure</title>
<link rel="stylesheet" href="https://fonts.googleapis.com/css2?family=Cinzel:wght@400;600&family=Open+Sans:wght@400;600;700&display=swap">
<style>
  :root{
    --green-deep:#005c33;
    --green:#0b8a4a;
    --green-bright:#3fbf5f;
    --green-light:#9fe07a;
    --teal:#00a990;
    --ink:#222;
    --bar:#1b1b1b;
    --paper:#ffffff;
    --backdrop:#dcdcdc;
  }
  *{box-sizing:border-box;margin:0;padding:0}
  html,body{width:1200px;height:856px;overflow:hidden}
  body{background:var(--backdrop);position:relative;font-family:"Open Sans",Arial,sans-serif;color:var(--ink)}
  .page{position:absolute;top:53px;width:526px;height:755px;background:var(--paper);overflow:hidden;box-shadow:0 2px 6px rgba(0,0,0,.25)}
  .page--cover{left:58px}
  .page--back{left:624px}

  .brand{position:absolute;display:flex;align-items:center;gap:10px;z-index:3}
  .brand__mark{width:30px;height:30px;background:var(--green-deep)}
  .brand__name{font-family:"Cinzel",Georgia,serif;font-weight:600;font-size:25px;color:var(--green-deep);letter-spacing:.5px;white-space:nowrap}
  .page--cover .brand{left:34px;top:50px}
  .page--back .brand{left:0;right:0;top:104px;justify-content:center}

  .cover-photo{position:absolute;left:0;top:100px;width:526px;height:610px;z-index:1;
    background:
      radial-gradient(ellipse at 55% 75%,#b9b9a8 0%,#8b8f80 10%,transparent 28%),
      linear-gradient(180deg,#2f4a1c 0%,#4f6f2a 30%,#3b5a22 55%,#2a3c19 100%)}
  .cover-waves{position:absolute;left:0;top:0;width:526px;height:755px;z-index:2}

  .cover-title{position:absolute;right:0;top:548px;z-index:3;background:rgba(255,255,255,.72);
    font-family:"Cinzel",Georgia,serif;font-weight:400;font-size:22px;line-height:31px;color:#2b2b2b;
    text-align:right;padding:6px 12px 6px 16px;white-space:nowrap}

  .url-bar{position:absolute;left:0;bottom:0;width:100%;height:40px;background:var(--bar);color:#fff;z-index:3;
    font-weight:600;font-size:15px;letter-spacing:3px;display:flex;align-items:center;justify-content:center}

  .back-swoosh{position:absolute;left:0;top:0;width:526px;height:120px}

  .contact{position:absolute;left:0;right:0;top:205px;text-align:center;font-size:14.5px;line-height:19px}
  .contact p{margin:0}
  .contact .web,.contact .mail{color:var(--green)}
  .contact .gap{margin-top:10px}
  .contact .address{font-size:11px;margin-top:4px}
  .contact .address b{color:var(--green)}

  .disclosure-heading{position:absolute;left:35px;top:352px;font-size:12.5px;font-weight:700}
  .disclosure{position:absolute;left:35px;top:376px;width:452px;height:310px;background:var(--green);color:#fff;
    padding:12px 12px;font-size:7.1px;line-height:1.46;text-align:justify;
    box-shadow:0 0 0 1px rgba(0,0,0,.05)}
  .disclosure p+p{margin-top:9px}
</style>
</head>
<body>

<section class="page page--cover">
  <div class="cover-photo" role="img" aria-label="Photograph of a wooden footbridge leading into a lush green forest"></div>

  <svg class="cover-waves" viewBox="0 0 526 755" aria-hidden="true">
    <defs>
      <linearGradient id="gTop" x1="0" y1="0" x2="1" y2="0">
        <stop offset="0" stop-color="#1f9a45"/><stop offset=".6" stop-color="#6fd66a"/><stop offset="1" stop-color="#c4f09a"/>
      </linearGradient>
      <linearGradient id="gBottom" x1="0" y1="1" x2="1" y2="0">
        <stop offset="0" stop-color="#005c33"/><stop offset=".5" stop-color="#22a24a"/><stop offset="1" stop-color="#8fe07a"/>
      </linearGradient>
    </defs>
    <path d="M0 0H526V108C430 92 330 120 220 142C140 158 60 166 0 162Z" fill="#fff"/>
    <path d="M0 162C60 166 140 158 220 142C330 120 430 92 526 108V124C430 110 330 138 220 158C140 174 60 180 0 176Z" fill="url(#gTop)"/>
    <path d="M0 176C60 180 140 174 220 158C330 138 430 110 526 124V130C430 118 330 144 220 164C140 180 60 186 0 182Z" fill="#e9f8df"/>
    <path d="M0 560C90 640 220 690 526 640V715H0Z" fill="url(#gBottom)"/>
    <path d="M0 600C110 670 250 700 526 668V715H0Z" fill="#eaf7e4" opacity=".9"/>
    <path d="M0 640C120 690 280 712 526 690V715H0Z" fill="#fff"/>
  </svg>

  <div class="brand"><span class="brand__mark"></span><span class="brand__name">Harlow Bend Partners</span></div>

  <h1 class="cover-title">Investment Strategies<br>That Match Your Goals</h1>

  <div class="url-bar">www.harlowbendpartners.com</div>
</section>

<section class="page page--back">
  <svg class="back-swoosh" viewBox="0 0 526 120" aria-hidden="true">
    <path d="M0 0H526V40C420 20 300 70 160 66C90 64 40 50 0 38Z" fill="#f1f1f1"/>
    <path d="M0 38C40 50 90 64 160 66C300 70 420 20 526 40V46C420 28 300 78 160 74C90 72 40 58 0 46Z" fill="#dedede"/>
  </svg>

  <div class="brand"><span class="brand__mark"></span><span class="brand__name">Harlow Bend Partners</span></div>

  <div class="contact">
    <p>visit us at <span class="web">www.HarlowBendPartners.com</span></p>
    <p>Call 877-555-0142 to speak with an investment Consultant</p>
    <p class="gap"><span class="mail">Email:&nbsp; info@harlowbendpartners.com</span></p>
    <p>to request more information or schedule and appointment</p>
    <p class="address"><b>ADDRESS:</b> Harlow Bend Partners, LLC 48 Meridian Drive Calder Falls PA 19250</p>
  </div>

  <h2 class="disclosure-heading">Disclosures Related to Harlow Bend Partners LLC</h2>

  <div class="disclosure">
    <p>In general the ETF-based Harlow Bend portfolios seek to outperform their benchmarks by raising and lowering exposure to asset classes, industry sectors, countries and currencies as relative prices change. To this end, the portfolios may use fixed income ETFs, equity ETFs, international ETFs, currency ETFs and alternative asset ETFs, including real estate, commodities and hedge fund strategies, and may adjust these holdings when appropriate. There are risks involved in investing in ETFs, including possible loss of money. Index-based ETFs are not actively managed, and actively managed ETFs do not necessarily seek to replicate the performance of a specified index. Both index-based and actively managed ETFs are subject to risks similar to stocks, including those related to short selling and margin maintenance. International investments may involve risk of capital loss from unfavorable currency movements, from differences in accounting principles, or from economic or political instability in other nations. Emerging markets involve heightened risks related to the same factors as well as increased volatility and lower trading volume. Investments in smaller companies, narrowly focused sectors and individual foreign countries typically exhibit higher volatility. Real estate investments are subject to changes in economic conditions, credit risk and interest rate fluctuations. Commodity-related investments are speculative and involve a high degree of risk. Bond and bond fund values will decrease in value as interest rates rise. Investment return and principal value will fluctuate so that shares, when sold or redeemed, may be worth more or less than their original cost. Income from tax-exempt securities may be subject to state or local taxes or the alternative minimum tax.</p>
    <p>This document does not constitute a recommendation or solicitation to buy or sell any security or investment strategy mentioned here. Any offer to invest in the firm's strategies can be made only by a written agreement. The information is intended for U.S. residents only. Before investing, an investor should carefully consider the portfolio objectives, risks, charges and expenses. For more information on Harlow Bend Partners, its investment strategies and how to invest, please contact the firm at 610-555-0187.</p>
  </div>

  <div class="url-bar">www.harlowbendpartners.com</div>
</section>

</body>
</html>
```